Flyer für Beratung, Planung und Montage von Photovoltaikanlagen, Wallboxen usw.
Der Ablauf war optimal. Auf Änderungswünsche wurde umgehend eingegangen. Die Bearbeitung erfolgt sehr zeitnah. Wir sind sehr zufrieden und können TOLVERIKO nur empfehlen.
Zielgruppe
Individuelle Beratung, Planung und Montage von Photovoltaikanlagen, Wallboxen, Balkonkraftwerke, PowerToHeat, Stromspeicher etc., (Neuanlagen & Bestandsanlagen), Privat- & Firmenkunden
Aufgabenstellung
Qualitativ hochwertige Markenprodukte, Seriös, Modern, Regionaler Anbieter, Flyer für gezielte regionale Verteilung (Briefkasten)

```html
<!DOCTYPE html>
<html lang="de">
<head>
<meta charset="utf-8">
<title>ISAR VOLTA – Erneuerbare Energien Flyer</title>
<link rel="stylesheet" href="https://fonts.googleapis.com/css2?family=Bebas+Neue&family=Roboto+Condensed:wght@400;700&family=Roboto:wght@400&display=swap">
<style>
  :root {
    --lime: #c8d419;
    --slate: #4d5654;
    --mist: #c8cac9;
    --stone: #9a9d9c;
    --paper: #ffffff;
  }
  html, body { margin: 0; padding: 0; overflow: hidden; background: var(--paper); }
  .flyer {
    position: relative; width: 1200px; height: 851px; overflow: hidden;
    background: var(--paper); font-family: "Roboto Condensed", Arial, sans-serif; color: var(--slate);
  }
  .frame { position: absolute; inset: 0; }
  .headline {
    position: absolute; left: 0; right: 0; top: 118px; margin: 0; text-align: center;
    font-family: "Bebas Neue", "Roboto Condensed", sans-serif; font-weight: 400;
    font-size: 92px; line-height: 80px; color: var(--lime); white-space: nowrap;
  }
  .services-title {
    position: absolute; left: 0; right: 0; top: 290px; margin: 0; text-align: center;
    font-size: 36px; font-weight: 700; line-height: 40px; letter-spacing: 0.3px;
  }
  .service { position: absolute; width: 500px; }
  .service-dot {
    position: absolute; left: -89px; top: 0; width: 68px; height: 68px;
    border-radius: 50%; background: var(--lime);
  }
  .service-name { margin: 0; font-size: 34px; line-height: 37px; font-weight: 700; white-space: nowrap; }
  .service-text { margin: 4px 0 0; font-size: 21px; line-height: 28px; color: var(--stone); white-space: nowrap; }
  .s-pv { left: 137px; top: 353px; }
  .s-storage { left: 725px; top: 356px; }
  .s-storage .service-text { margin-left: 4px; }
  .s-charge { left: 137px; top: 455px; }
  .s-service { left: 725px; top: 455px; }
  .s-pv .service-dot, .s-storage .service-dot { top: -6px; }
  .s-storage .service-dot { top: -9px; }
  .s-charge .service-dot, .s-service .service-dot { top: 0; }
  .cta-text {
    position: absolute; left: 28px; top: 644px; margin: 0;
    font-size: 31px; line-height: 33px; font-weight: 700; color: var(--paper);
  }
  .cta-phone {
    position: absolute; left: 262px; top: 636px; width: 140px; text-align: center;
    font-size: 28px; line-height: 29px; font-weight: 700; color: var(--paper);
  }
  .brand {
    position: absolute; left: 948px; top: 696px; display: flex; align-items: center; gap: 10px;
    font-family: "Roboto Condensed", Arial, sans-serif; font-weight: 400;
    font-size: 34px; letter-spacing: 2px; color: var(--slate);
  }
  .brand-dot { width: 22px; height: 22px; border-radius: 50%; background: var(--lime); }
  .address {
    position: absolute; left: 24px; top: 804px; margin: 0;
    font-family: "Roboto", Arial, sans-serif; font-size: 17px; color: var(--slate);
  }
  .website {
    position: absolute; left: 860px; top: 798px; margin: 0;
    font-family: "Roboto", Arial, sans-serif; font-size: 31px; color: var(--paper);
  }
</style>
</head>
<body>
<div class="flyer">
  <svg class="frame" width="1200" height="851" viewBox="0 0 1200 851" aria-hidden="true">
    <!-- top bands -->
    <path d="M0 0 H1200 V19 H600 C540 19 520 95 430 95 H0 Z" fill="var(--mist)"/>
    <path d="M0 0 H550 C500 0 480 65 420 65 H0 Z" fill="var(--slate)"/>
    <!-- bottom right bands -->
    <path d="M620 851 C700 851 710 756 800 756 H1200 V851 Z" fill="var(--mist)"/>
    <path d="M632 851 C710 851 720 781 800 781 H1200 V851 Z" fill="var(--slate)"/>
    <!-- bottom left strip -->
    <rect x="0" y="830" width="660" height="21" fill="var(--mist)"/>
    <!-- call to action band -->
    <path d="M0 620 H328 A80 80 0 0 1 328 780 H0 Z" fill="var(--slate)"/>
    <circle cx="331" cy="700" r="75" fill="var(--paper)"/>
    <circle cx="331" cy="700" r="69" fill="var(--lime)"/>
  </svg>

  <h1 class="headline">Hallo, wir sind Ihr regionaler<br>Anbieter für erneuerbare Energien.</h1>
  <h2 class="services-title">UNSERE LEISTUNGEN:</h2>

  <div class="service s-pv">
    <span class="service-dot"></span>
    <h3 class="service-name">PHOTOVOLTAIKANLAGEN</h3>
    <p class="service-text">360° Service rund um ihre PV-Anlage</p>
  </div>
  <div class="service s-storage">
    <span class="service-dot"></span>
    <h3 class="service-name">STROMSPEICHER</h3>
    <p class="service-text">Privat- oder Gewerbespeicher für alle Bedürfniss</p>
  </div>
  <div class="service s-charge">
    <span class="service-dot"></span>
    <h3 class="service-name">LADEINFRASTRUKTUR<br>UND ELEKTROMOBILITÄT:</h3>
    <p class="service-text">Ob Wallbox mit Überschussladen, oder mehrere mit<br>intelligentem Lastmanagement, Ladepark oder Tiefgarage</p>
  </div>
  <div class="service s-service">
    <span class="service-dot"></span>
    <h3 class="service-name">WARTUNG - SERVICE<br>UND MONITORING</h3>
    <p class="service-text">Wir informieren Sie sofort, wenn mit Ihrer Anlage<br>etwas nicht stimmt</p>
  </div>

  <p class="cta-text">Jetzt unverbl.<br>Beratungstermin<br>vereinbaren</p>
  <div class="cta-phone">Tel.:<br>08231<br>4472100</div>

  <div class="brand"><span class="brand-dot"></span>ISAR VOLTA</div>

  <p class="address">ISAR VOLTA GmbH · Birkenstr. 9B · 86899 Talhofen</p>
  <p class="website">www.isarvolta.de</p>
</div>
</body>
</html>
```